Wordpress website design for membership site

I need a wordpress website designed for a membership site specializing in member video recordings and storage. I need the site to be simplistic but fully functional. I want a minimalistic landing and member page. The member page needs to be able to showcase the members recorded videos amd utilize a GUI system of navigation utilizing graphical buttons. Member signup page needs to be fully functional to include email verification and password change/recovery functionality.

Coding

Coded - Design and coding required

Number of Pages Required

3 page

Font styles to use
Sans Serif

Colors

Designer to choose colors to be used in the design.

Requirements
Must have
• The project must incorporate the name ZELQON or ZELQON.com within the design.
Should not have
• Project should not use prepublished templates available online but should be unique in design and functionality.

```html
<!DOCTYPE html>
<html lang="en">
<head>
<meta charset="utf-8">
<title>ZELQON — Member Video Home</title>
<link href="https://fonts.googleapis.com/css2?family=Poppins:wght@400;500;600;700;800;900&display=swap" rel="stylesheet">
<style>
:root{
  --green:#2bb673;
  --green-dark:#1f9a5e;
  --green-soft:#5fd39b;
  --ink:#151515;
  --text:#555;
  --muted:#8a8a8a;
  --line:#dcdcdc;
  --paper:#ffffff;
  --gray:#efefef;
  --gray-2:#f5f5f5;
  --band-a:#262d78;
  --band-b:#3d1d66;
}
*{box-sizing:border-box;margin:0;padding:0}
html,body{width:1200px;height:5263px;overflow:hidden;background:var(--paper)}
body{font-family:'Poppins',sans-serif;color:var(--ink);position:relative}
.abs{position:absolute}
.hero{position:absolute;left:0;top:0;width:1200px;height:604px;
  background:linear-gradient(100deg,#f7f8f7 0%,#eef0ee 35%,#d9dcd8 60%,#c9c7bf 100%)}
.hero-photo{position:absolute;left:560px;top:0;width:640px;height:604px;
  background:radial-gradient(ellipse at 55% 50%,#a9a59b 0%,#cfcbc2 45%,rgba(230,232,228,0) 75%)}
.logo{position:absolute;display:flex;align-items:center;gap:10px;font-weight:800;font-size:30px;color:var(--green);letter-spacing:1px}
.logo .mark{width:22px;height:22px;background:var(--green)}
.nav-btn{position:absolute;top:30px;height:32px;border-radius:16px;font-size:11px;font-weight:600;
  display:flex;align-items:center;justify-content:center;letter-spacing:.5px}
.nav-outline{left:826px;width:162px;border:2px solid var(--green);color:var(--ink);background:rgba(255,255,255,.6)}
.nav-fill{left:998px;width:82px;background:var(--green);color:#fff}
.burger{position:absolute;left:1096px;top:38px;width:28px}
.burger i{display:block;height:3px;background:var(--ink);margin-bottom:5px;border-radius:2px}
.eyebrow{left:163px;top:212px;font-size:12px;font-weight:500;color:var(--ink)}
.eyebrow-green{left:163px;top:229px;font-size:15px;font-weight:700;color:var(--green)}
.hero-title{left:158px;top:240px;font-size:96px;font-weight:900;letter-spacing:-2px;line-height:1.05}
.hero-title span{color:var(--green)}
.hero-sub{left:163px;top:340px;font-size:26px;font-weight:500;letter-spacing:.5px}
.btn{position:absolute;border-radius:22px;font-size:11px;font-weight:600;display:flex;align-items:center;justify-content:center;letter-spacing:.5px}
.btn-green{background:var(--green);color:#fff}
.btn-outline{border:2px solid var(--green);color:var(--ink)}
.notch{position:absolute;left:540px;width:120px;height:34px}
.sec-head{position:absolute;font-size:19px;font-weight:700;letter-spacing:.3px}
.sec-note{position:absolute;font-size:10px;color:var(--muted)}
.arrows{position:absolute;font-size:16px;color:#bbb;letter-spacing:10px}
.card-img{position:absolute;width:228px;height:257px}
.tag-new{position:absolute;background:#e53935;color:#fff;font-size:9px;font-weight:700;padding:2px 6px}
.card-title{position:absolute;width:228px;text-align:center;font-size:14px;font-weight:600;line-height:1.3}
.card-meta{position:absolute;width:228px;text-align:center;font-size:10px;color:var(--muted)}
.band{position:absolute;left:147px;width:902px;height:86px;
  background:linear-gradient(90deg,var(--band-a),#2d2a80 50%,var(--band-b))}
.band-text{position:absolute;left:42px;top:24px;font-size:29px;font-weight:700;color:#fff}
.band-btn{position:absolute;right:40px;top:29px;width:150px;height:30px;border-radius:15px;background:var(--green);color:#fff;font-size:11px;font-weight:600;display:flex;align-items:center;justify-content:center}
.about-title{left:147px;top:1318px;font-size:30px;font-weight:700;line-height:1.35;width:430px}
.about-title span{color:var(--green)}
.about-copy{left:624px;top:1318px;width:420px;font-size:12px;line-height:1.75;color:var(--text)}
.about-copy p{margin-bottom:14px}
.about-photo{left:0;top:1500px;width:1200px;height:395px;
  background:linear-gradient(180deg,rgba(255,255,255,1) 0%,#d6dce0 30%,#b9b0a3 70%,#e9e2d8 100%)}
.trend-head{left:0;width:1200px;top:1945px;text-align:center;font-size:19px;font-weight:700}
.trend-note{left:0;width:1200px;top:1975px;text-align:center;font-size:10px;color:var(--muted)}
.tile{position:absolute}
.tile-label{position:absolute;left:18px;bottom:18px;color:#fff}
.tile-label b{display:block;font-size:15px;font-weight:700}
.tile-label small{font-size:10px}
.latest-bg{left:0;top:2614px;width:1200px;height:983px;background:var(--gray)}
.thumb{position:absolute;width:171px;height:225px}
.thumb-cap{position:absolute;width:171px;text-align:center;font-size:13px;font-weight:500}
.stats-bg{left:0;top:3597px;width:1200px;height:491px;
  background:linear-gradient(90deg,#2bb673 0%,#3a9c7a 40%,#3b9078 60%,#2bb673 100%)}
.quote-card{position:absolute;width:305px;height:225px;border:2px solid rgba(255,255,255,.45)}
.avatar{position:absolute;width:112px;height:130px}
.q-name{position:absolute;color:#fff;font-size:16px;font-weight:600}
.q-role{position:absolute;color:rgba(255,255,255,.85);font-size:10px}
.q-text{position:absolute;color:#fff;font-size:11px;line-height:1.6;width:200px}
.q-mark{position:absolute;color:#fff;font-size:44px;font-weight:900;line-height:1}
.counter{position:absolute;width:220px;text-align:center}
.counter .circle{width:96px;height:96px;border-radius:50%;background:var(--green);margin:0 auto;display:flex;align-items:center;justify-content:center}
.counter .num{font-size:42px;font-weight:700;margin-top:30px;line-height:1}
.counter .lbl{font-size:11px;font-weight:600;color:var(--green);letter-spacing:4px;margin-top:8px}
.contact-bg{left:0;top:4456px;width:1200px;height:492px;background:var(--gray-2)}
.device{position:absolute}
.contact-head{left:0;width:1200px;top:4532px;text-align:center;font-size:30px;font-weight:700}
.contact-head span{color:var(--green)}
.contact-note{left:0;width:1200px;top:4576px;text-align:center;font-size:11px;color:var(--muted)}
.field{position:absolute;background:#fff;border:1px solid var(--line);font-size:11px;color:#aaa;padding:12px 14px}
.foot-links{left:0;width:1200px;top:5160px;display:flex;justify-content:center;gap:26px;font-size:12px;font-weight:500}
.social{left:0;width:1200px;top:5130px;display:flex;justify-content:center;gap:18px}
.social i{width:14px;height:14px;border-radius:50%;background:var(--ink);display:block}
.copyright{left:0;width:1200px;top:5200px;text-align:center;font-size:10px;color:var(--muted)}
</style>
</head>
<body>

<section class="hero">
  <div class="hero-photo" role="img" aria-label="Photo of a young man in headphones singing into his phone while lounging in a wicker chair"></div>
  <div class="logo" style="left:110px;top:26px"><span class="mark"></span>ZELQON</div>
  <div class="nav-btn nav-outline">BECOME A MEMBER</div>
  <div class="nav-btn nav-fill">LOGIN</div>
  <div class="burger"><i></i><i></i><i></i></div>
  <div class="abs eyebrow">ARE YOU READY TO</div>
  <div class="abs eyebrow-green">UPLOAD VIDEO TODAY!</div>
  <h1 class="abs hero-title">FEEL <span>GOOD</span></h1>
  <div class="abs hero-sub">LOREM IPSUM IS SIMPLY</div>
  <div class="btn btn-green" style="left:163px;top:393px;width:170px;height:42px">JOIN US TODAY!</div>
</section>
<svg class="notch" style="top:570px" viewBox="0 0 120 34"><path d="M0 34 C30 34 35 4 60 4 C85 4 90 34 120 34Z" fill="#fff"/><path d="M53 18 L60 25 L67 18" stroke="#2bb673" stroke-width="2.5" fill="none"/></svg>

<h2 class="sec-head" style="left:147px;top:686px">POPULAR VIDEOS</h2>
<div class="sec-note" style="left:344px;top:693px">Lorem ipsum is simply dummy text of the printing and</div>
<div class="arrows" style="left:1012px;top:686px">‹›</div>

<div class="card-img" style="left:147px;top:761px;background:linear-gradient(160deg,#2a3a55,#1a2233 60%,#46586c)" role="img" aria-label="Photo of a woman singing on stage"></div>
<div class="tag-new" style="left:155px;top:768px">NEW</div>
<div class="card-img" style="left:379px;top:761px;background:linear-gradient(160deg,#2bb673,#1f9a5e)" role="img" aria-label="Video thumbnail with green overlay and play button"></div>
<svg class="abs" style="left:463px;top:859px" width="60" height="60" viewBox="0 0 60 60"><circle cx="30" cy="30" r="26" stroke="#fff" stroke-width="2" fill="none"/><path d="M25 19 L41 30 L25 41Z" fill="#fff"/></svg>
<div class="card-img" style="left:611px;top:761px;background:linear-gradient(160deg,#1c1635,#3a2b6a 50%,#0f0d1c)" role="img" aria-label="Photo of a DJ in a hoodie under stage lights"></div>
<div class="tag-new" style="left:619px;top:768px">NEW</div>
<div class="card-img" style="left:846px;top:761px;background:linear-gradient(160deg,#8a6e5c,#5a4434 60%,#b49a82)" role="img" aria-label="Photo of two friends filming themselves"></div>
<div class="tag-new" style="left:854px;top:768px">NEW</div>

<div class="card-title" style="left:147px;top:1030px">Lorem Ipsum is simply<br>dummy text of the</div>
<div class="card-meta" style="left:147px;top:1077px">LOREM IPSUM IS</div>
<div class="card-title" style="left:379px;top:1030px">Lorem Ipsum is simply<br>dummy text of the</div>
<div class="card-meta" style="left:379px;top:1077px">LOREM IPSUM IS</div>
<div class="card-title" style="left:611px;top:1030px">Lorem Ipsum is simply<br>dummy text of the</div>
<div class="card-meta" style="left:611px;top:1077px">LOREM IPSUM IS</div>
<div class="card-title" style="left:846px;top:1030px">Lorem Ipsum is simply<br>dummy text of the</div>
<div class="card-meta" style="left:846px;top:1077px">LOREM IPSUM IS</div>

<div class="band" style="top:1168px"><div class="band-text">Telling stories that make a difference</div><div class="band-btn">JOIN US TODAY!</div></div>

<div class="abs about-photo" role="img" aria-label="Photo of a smiling woman in headphones holding her phone against a blurred city skyline"></div>
<h2 class="abs about-title">LOREM IPSUM IS SIMPLY DUMMY TEXT OF <span>THE PRINTING AND TYPESETTING.</span></h2>
<div class="btn btn-outline" style="left:147px;top:1457px;width:128px;height:30px;font-size:10px">READ MORE</div>
<div class="abs about-copy">
  <p>Lorem Ipsum is simply dummy text of the printing and typesetting industry. Lorem Ipsum has been the industry's standard dummy text ever since the 1500s, when an unknown printer took a galley.</p>
  <p>Of type and scrambled it to make a type specimen book. It has survived not only five centuries, but also the leap into electronic.</p>
  <p>Typesetting, remaining essentially unchanged. It was popularised in the 1960s with the release of transfer sheets containing Lorem Ipsum passages, and more recently with desktop.</p>
</div>

<h2 class="abs trend-head">TRENDING VIDEOS</h2>
<div class="abs trend-note">Lorem ipsum is simply dummy text of the printing and</div>
<div class="abs" style="left:470px;top:1998px;width:260px;height:1px;background:var(--line)"></div>

<div class="tile" style="left:158px;top:2042px;width:295px;height:439px;background:linear-gradient(180deg,#3a1f10,#9b4a18 35%,#2a1409 80%)" role="img" aria-label="Photo of a singer on a stage under orange lights"><div class="tile-label"><b>DUMMY HEADING</b><small>120 VIDEOS</small></div></div>
<div class="tile" style="left:453px;top:2042px;width:294px;height:220px;background:linear-gradient(160deg,#c9924d,#8a5a2a 60%,#d6a467)" role="img" aria-label="Photo of a woman playing acoustic guitar"><div class="tile-label"><b>DUMMY HEADING</b><small>120 VIDEOS</small></div></div>
<div class="tile" style="left:453px;top:2262px;width:294px;height:219px;background:linear-gradient(160deg,#2a3f9a,#4b2d8a 60%,#1e2a6a)" role="img" aria-label="Photo of a woman singing into a microphone under blue light"></div>
<div class="tile" style="left:747px;top:2042px;width:292px;height:439px;background:linear-gradient(180deg,#5d6770,#2c3238 60%,#1a1e22)" role="img" aria-label="Photo of a young man with an electric guitar"><div class="tile-label"><b>DUMMY HEADING</b><small>120 VIDEOS</small></div></div>

<div class="abs latest-bg"></div>
<svg class="notch" style="top:2580px" viewBox="0 0 120 34"><path d="M0 34 C30 34 35 4 60 4 C85 4 90 34 120 34Z" fill="#efefef"/><path d="M53 18 L60 25 L67 18" stroke="#2bb673" stroke-width="2.5" fill="none"/></svg>
<h2 class="sec-head" style="left:147px;top:2708px">LATEST VIDEOS</h2>
<div class="sec-note" style="left:344px;top:2715px">Lorem ipsum is simply dummy text of the printing and</div>
<div class="arrows" style="left:1012px;top:2708px">‹›</div>

<div class="thumb" style="left:147px;top:2793px;background:linear-gradient(160deg,#3a2a22,#1a1410)" role="img" aria-label="Photo of a woman singing"></div>
<div class="thumb" style="left:333px;top:2793px;background:linear-gradient(160deg,#6a3a9a,#c04a8a 60%,#2a2a6a)" role="img" aria-label="Photo of a performer under purple lights"></div>
<div class="thumb" style="left:519px;top:2793px;background:linear-gradient(160deg,#f0d020,#e8b810)" role="img" aria-label="Photo of a woman singing against a yellow wall"></div>
<div class="thumb" style="left:698px;top:2793px;background:linear-gradient(160deg,#1a2a4a,#3a1a3a 60%,#0e1424)" role="img" aria-label="Photo of a man singing into a microphone"></div>
<div class="thumb" style="left:881px;top:2793px;background:linear-gradient(160deg,#d8d2c8,#a89a88)" role="img" aria-label="Photo of a man listening with headphones"></div>
<div class="thumb-cap" style="left:147px;top:3032px">Velvet Voice</div>
<div class="thumb-cap" style="left:333px;top:3032px">Hopzo Edition Dude</div>
<div class="thumb-cap" style="left:519px;top:3032px">Velvet Voice</div>
<div class="thumb-cap" style="left:698px;top:3032px">Hopzo Edition Dude</div>
<div class="thumb-cap" style="left:881px;top:3032px">Velvet Voice</div>

<div class="thumb" style="left:147px;top:3077px;background:linear-gradient(160deg,#c88a6a,#e8c4a8)" role="img" aria-label="Photo of a laughing woman"></div>
<div class="thumb" style="left:333px;top:3077px;background:linear-gradient(160deg,#c8b8a8,#7a6a5a)" role="img" aria-label="Photo of a man with a guitar"></div>
<div class="thumb" style="left:519px;top:3077px;background:linear-gradient(160deg,#c8403a,#e8e0d0 60%,#8a2a2a)" role="img" aria-label="Photo of vinyl records on a table"></div>
<div class="thumb" style="left:698px;top:3077px;background:linear-gradient(160deg,#4a5a3a,#8a8a6a)" role="img" aria-label="Photo of a man singing outdoors"></div>
<div class="thumb" style="left:881px;top:3077px;background:linear-gradient(160deg,#b88a5a,#7a5a3a)" role="img" aria-label="Photo of a smiling man with a tablet"></div>
<div class="thumb-cap" style="left:147px;top:3312px">Velvet Voice</div>
<div class="thumb-cap" style="left:333px;top:3312px">Hopzo Edition Dude</div>
<div class="thumb-cap" style="left:519px;top:3312px">Velvet Voice</div>
<div class="thumb-cap" style="left:698px;top:3312px">Hopzo Edition Dude</div>
<div class="thumb-cap" style="left:881px;top:3312px">Velvet Voice</div>

<div class="band" style="top:3414px"><div class="band-text">Telling stories that make a difference</div><div class="band-btn">JOIN US TODAY!</div></div>

<div class="abs stats-bg" role="img" aria-label="Green-tinted photo of a video camera on a tripod"></div>
<svg class="notch" style="top:3563px" viewBox="0 0 120 34"><path d="M0 34 C30 34 35 4 60 4 C85 4 90 34 120 34Z" fill="#2bb673"/><path d="M53 18 L60 25 L67 18" stroke="#fff" stroke-width="2.5" fill="none"/></svg>
<h2 class="sec-head" style="left:147px;top:3662px;color:#fff">BIGGEST STATISTICS</h2>
<div class="sec-note" style="left:368px;top:3669px;color:rgba(255,255,255,.8)">Lorem ipsum is simply dummy text of the printing and</div>
<div class="abs" style="left:128px;top:3862px;color:#fff;font-size:22px">←</div>
<div class="abs" style="left:1048px;top:3862px;color:#fff;font-size:22px">→</div>

<div class="quote-card" style="left:270px;top:3765px"></div>
<div class="avatar" style="left:180px;top:3772px;background:linear-gradient(160deg,#3a3a8a,#c04a6a)" role="img" aria-label="Portrait photo of a singing woman"></div>
<div class="q-name" style="left:330px;top:3814px">Lorem Ipsum simply</div>
<div class="q-role" style="left:330px;top:3838px">Dummy Text, Head of - UK</div>
<div class="q-mark" style="left:294px;top:3862px">“</div>
<div class="q-text" style="left:330px;top:3870px">Lorem Ipsum is simply dummy text of the printing and typesetting industry. Lorem Ipsum has been</div>

<div class="quote-card" style="left:705px;top:3765px"></div>
<div class="avatar" style="left:615px;top:3772px;background:linear-gradient(160deg,#c8a888,#6a5040)" role="img" aria-label="Portrait photo of a man"></div>
<div class="q-name" style="left:765px;top:3814px">Lorem Ipsum simply</div>
<div class="q-role" style="left:765px;top:3838px">Dummy Text, Head of - UK</div>
<div class="q-mark" style="left:729px;top:3862px">“</div>
<div class="q-text" style="left:765px;top:3870px">Lorem Ipsum is simply dummy text of the printing and typesetting industry. Lorem Ipsum has been</div>
<svg class="notch" style="top:4054px" viewBox="0 0 120 34"><path d="M0 34 C30 34 35 4 60 4 C85 4 90 34 120 34Z" fill="#fff"/><path d="M53 18 L60 25 L67 18" stroke="#2bb673" stroke-width="2.5" fill="none"/></svg>

<div class="counter" style="left:188px;top:4180px">
  <div class="circle"><svg width="44" height="34" viewBox="0 0 44 34" fill="none" stroke="#fff" stroke-width="2.5"><circle cx="22" cy="10" r="6"/><path d="M10 32 C10 22 34 22 34 32"/><circle cx="8" cy="14" r="4"/><circle cx="36" cy="14" r="4"/></svg></div>
  <div class="num">170430</div><div class="lbl">USERS</div>
</div>
<div class="counter" style="left:486px;top:4180px">
  <div class="circle"><svg width="42" height="34" viewBox="0 0 42 34" fill="none" stroke="#fff" stroke-width="2.5"><rect x="3" y="3" width="36" height="24" rx="2"/><path d="M17 10 L26 15 L17 20Z" fill="#fff"/><path d="M14 32 H28"/></svg></div>
  <div class="num">260938</div><div class="lbl">VIDEOS</div>
</div>
<div class="counter" style="left:785px;top:4180px">
  <div class="circle"><svg width="40" height="36" viewBox="0 0 40 36" fill="none" stroke="#fff" stroke-width="2.5"><path d="M4 16 H11 V33 H4Z"/><path d="M11 17 L19 4 C22 4 23 6 22 10 L21 14 H33 C36 14 37 17 36 19 L32 31 C31 33 30 33 28 33 H11"/></svg></div>
  <div class="num">70430</div><div class="lbl">REVIEWS</div>
</div>

<div class="abs contact-bg"></div>
<svg class="notch" style="top:4422px" viewBox="0 0 120 34"><path d="M0 34 C30 34 35 4 60 4 C85 4 90 34 120 34Z" fill="#f5f5f5"/><path d="M53 18 L60 25 L67 18" stroke="#2bb673" stroke-width="2.5" fill="none"/></svg>
<div class="device" style="left:0;top:4456px;width:210px;height:170px;background:linear-gradient(160deg,#9a9a9a,#d8d8d8)" role="img" aria-label="Photo of a laptop corner"></div>
<div class="device" style="left:80px;top:4760px;width:190px;height:160px;background:radial-gradient(circle,#2a2a2a 30%,rgba(245,245,245,0) 70%)" role="img" aria-label="Photo of a camera lens"></div>
<div class="device" style="left:1040px;top:4456px;width:160px;height:200px;background:radial-gradient(circle at 60% 40%,#2a2a2a 30%,rgba(245,245,245,0) 70%)" role="img" aria-label="Photo of headphones"></div>
<div class="device" style="left:960px;top:4760px;width:240px;height:170px;background:radial-gradient(circle at 60% 50%,#1e1e1e 30%,rgba(245,245,245,0) 70%)" role="img" aria-label="Photo of a camcorder"></div>

<h2 class="abs contact-head">GET IN <span>TOUCH</span></h2>
<div class="abs contact-note">Any questions or remarks? Just write us a message!</div>
<div class="field" style="left:302px;top:4639px;width:298px;height:44px">Name</div>
<div class="field" style="left:600px;top:4639px;width:298px;height:44px">Email Address</div>
<div class="field" style="left:302px;top:4683px;width:596px;height:108px">Message</div>
<div class="btn btn-green" style="left:527px;top:4820px;width:146px;height:32px;font-size:11px">SUBMIT NOW</div>

<div class="logo" style="left:0;width:1200px;justify-content:center;top:5045px"><span class="mark"></span>ZELQON</div>
<div class="abs social"><i></i><i></i><i></i><i></i></div>
<nav class="abs foot-links"><span>HOME</span><span>ABOUT US</span><span>LOGIN</span><span>TESTIMONIALS</span><span>CONTACT</span></nav>
<div class="abs copyright">© 2024 ZELQON.com. All rights reserved &nbsp;|&nbsp; Terms &amp; Conditions &nbsp;|&nbsp; Privacy Policy</div>

</body>
</html>
```